Economic Development Agency Needs a PowerPoint Design

We are a non profit economics development agency promotes Ontario as a top foreign direct invest destination for Chinese businesses. We also provide services for Chinese businesses investing in Ontario in partnership with Ontario and Municipal governments.

The final design should communicate corporate, financial safety and growth

Industry/Entity Type

Non Profit

```html
<!DOCTYPE html>
<html lang="en">
<head>
<meta charset="utf-8">
<title>Northgate Investment Council – Presentation Template</title>
<link href="https://fonts.googleapis.com/css2?family=Montserrat:wght@600;700&family=Roboto:wght@300;400;500;700&display=swap" rel="stylesheet">
<style>
:root{
  --red:#ed1c2a;
  --ink:#231f20;
  --dark:#3a3a3a;
  --darker:#2c2c2c;
  --grey-bg:#a7adb3;
  --paper:#f7f7f7;
  --white:#ffffff;
  --muted:#8a8a8a;
  --line:#e3e3e3;
  --blue:#00a0d6;
  --green:#74bd43;
  --orange:#e5723a;
  --purple:#9457ae;
}
*{box-sizing:border-box;margin:0;padding:0}
html,body{width:1058px;height:1200px;overflow:hidden;background:var(--grey-bg)}
body{font-family:'Roboto',sans-serif;color:var(--ink);position:relative}
.slide{position:absolute;width:514px;height:386px;background:var(--white);overflow:hidden}
.s1{left:11px;top:9px;background:var(--paper)}
.s2{left:533px;top:9px}
.s3{left:11px;top:403px}
.s4{left:533px;top:403px}
.s5{left:11px;top:799px}
.s6{left:533px;top:799px;background:var(--red)}

.brand-name{font-family:'Montserrat',sans-serif;font-weight:700;color:var(--red);text-align:center;line-height:1.05;letter-spacing:.5px}
.s1 .brand-name{position:absolute;left:0;right:0;top:122px;font-size:44px}
.s2 .brand-name{position:absolute;left:0;right:0;top:86px;font-size:34px}
.s6 .brand-name{position:absolute;left:0;right:0;top:96px;font-size:40px;color:var(--white)}

.deck-title{position:absolute;right:14px;top:280px;text-align:right}
.deck-title h2{font-weight:400;font-size:16px;color:var(--ink)}
.deck-title p{font-size:11px;color:var(--red);margin-top:2px}
.cover-band{position:absolute;left:0;right:0;bottom:0;height:62px;background:var(--ink);padding:14px 10px}
.cover-band h3{font-weight:300;font-size:17px;color:var(--white);letter-spacing:.3px}
.cover-band h3 b{font-weight:700}
.cover-band p{font-size:11px;color:var(--red);margin-top:2px}
.cover-band p b{font-weight:700}
.pic-badge{position:absolute;right:14px;top:12px;width:58px;height:40px;border:1px solid #5a1a1e;display:flex;align-items:center;justify-content:center}

.slide-head{height:48px;border-bottom:1px solid var(--line);text-align:center;padding-top:4px}
.slide-head h2{font-weight:400;font-size:23px;color:var(--red);letter-spacing:-.3px}
.slide-head p{font-size:7.5px;color:var(--muted);margin-top:1px;letter-spacing:.2px}
.slide-head p b{font-weight:700}

.foot{position:absolute;left:0;right:0;bottom:0;height:31px;background:var(--red);display:flex;align-items:center;padding:0 10px;color:var(--white)}
.foot .mark{font-weight:700;font-size:13px;margin-right:10px}
.foot .label{font-size:8.5px;font-weight:500;letter-spacing:.2px}
.foot .page{margin-left:auto;font-size:8px;margin-right:6px}
.foot.dark{background:var(--ink)}
.foot.dark .mark{color:var(--red)}

.photo-frame{position:absolute;left:35px;top:71px;width:446px;height:198px;border:1px solid var(--red);background:#e6e6e6;display:flex;align-items:center;justify-content:center}
.notes{position:absolute;left:35px;top:281px;width:460px}
.note{display:flex;gap:8px;margin-bottom:12px;align-items:flex-start}
.note svg{flex:none;margin-top:1px}
.note p{font-size:7px;line-height:1.4;color:#555}
.note b{color:var(--ink)}

.table-block{position:absolute;top:68px;width:230px}
.table-block.light{left:19px}
.table-block.dark{left:266px}
.table-title{display:flex;align-items:center;gap:5px;font-size:13.5px;font-weight:300;margin-bottom:10px}
.table-title b{font-weight:500}
table{width:100%;border-collapse:collapse;font-size:5.6px}
th{font-weight:400;font-size:7.5px;height:21px;text-align:left;padding:0 4px}
th:first-child,td:first-child{text-align:center;width:28px}
td{height:22.4px;padding:0 4px;border-bottom:1px solid var(--line);color:#666;line-height:1.3}
td:first-child{color:var(--red);font-size:8px}
td:last-child,th:last-child{text-align:center}
.light th{background:var(--dark);color:var(--white)}
.light .tfoot{background:var(--red)}
.dark th{background:var(--red);color:var(--white);font-weight:500}
.dark td{background:var(--dark);border-bottom-color:#2e2e2e;color:#aaa}
.dark .tfoot{background:var(--dark)}
.tfoot{height:22px;color:var(--white);font-size:8.5px;display:flex;align-items:center;justify-content:center}

.graph-title{position:absolute;top:70px;font-size:14.5px;font-weight:300;color:#555}
.graph-title b{font-weight:500;color:var(--ink)}
.g-main{left:26px}
.g-sec{left:293px}
.chart-area{position:absolute;left:20px;top:100px}
.chart-pie{position:absolute;left:290px;top:96px}
.bullets{position:absolute;top:278px;width:200px;list-style:none}
.bullets li{font-size:6.6px;line-height:1.45;color:#666;padding-left:12px;position:relative;margin-bottom:9px}
.bullets li::before{content:"";position:absolute;left:0;top:2px;border-left:3px solid var(--red);border-top:2px solid transparent;border-bottom:2px solid transparent}
.bullets b{color:var(--ink)}
.b-main{left:36px}
.b-sec{left:287px;width:210px}
.legend{position:absolute;left:440px;top:237px;display:grid;grid-template-columns:auto auto;gap:3px 8px;font-size:7px;color:#555}
.legend span{display:flex;align-items:center;gap:3px}
.legend i{width:7px;height:7px;border-radius:50%;display:inline-block}

.contact{position:absolute;left:14px;bottom:14px;color:var(--white);font-size:7px;line-height:1.45}
.contact h4{font-size:9px;font-weight:700;margin-top:12px}
.contact h4:first-child{margin-top:0}
.contact u{text-decoration:underline}
.social{position:absolute;right:18px;bottom:18px;display:flex;gap:9px;align-items:center}
.social i{width:12px;height:12px;border-radius:50%;background:var(--white);display:block}
</style>
</head>
<body>

<section class="slide s1">
  <h1 class="brand-name">Northgate<br>Investment Council</h1>
</section>

<section class="slide s2">
  <h1 class="brand-name">Northgate<br>Investment Council</h1>
  <div class="deck-title">
    <h2>PRESENTATION TITLE</h2>
    <p>JAN 2014</p>
  </div>
  <div class="cover-band">
    <h3><b>COMPANY</b> PRESENTATION</h3>
    <p>to <b>Business</b>/Client</p>
    <div class="pic-badge">
      <svg width="22" height="20" viewBox="0 0 22 20"><rect x="1" y="1" width="20" height="18" fill="none" stroke="#ed1c2a" stroke-width="2"/><circle cx="7" cy="7" r="2" fill="#ed1c2a"/><path d="M4 16 L9 10 L12 13 L15 9 L18 16Z" fill="#ed1c2a"/></svg>
    </div>
  </div>
</section>

<section class="slide s3">
  <header class="slide-head">
    <h2>IMAGE IN LANDSCAPE VIEW</h2>
    <p>WITH COMPLETELY <b>CUSTOMIZABLE</b> ICONS</p>
  </header>
  <div class="photo-frame" role="img" aria-label="Landscape photo placeholder">
    <svg width="94" height="94" viewBox="0 0 94 94"><rect x="3" y="3" width="88" height="88" fill="none" stroke="#dcdcdc" stroke-width="6"/><circle cx="28" cy="28" r="9" fill="#dcdcdc"/><path d="M12 80 L36 46 L48 62 L62 40 L82 80Z" fill="#dcdcdc"/></svg>
  </div>
  <div class="notes">
    <div class="note">
      <svg width="18" height="15" viewBox="0 0 18 15"><rect x="1" y="1" width="16" height="10" fill="none" stroke="#ed1c2a" stroke-width="2"/><rect x="7" y="11" width="4" height="2" fill="#ed1c2a"/><rect x="4" y="13" width="10" height="2" fill="#ed1c2a"/></svg>
      <p><b>Aenean</b> ridiculus tortor quis interdum id habitant ad, natoque consectetuer nisl auctor libero quisque euismod ante inceptos malesuada ligula mattis.</p>
    </div>
    <div class="note">
      <svg width="20" height="14" viewBox="0 0 20 14"><path d="M1 13 L7 7 L10 10 L17 3" fill="none" stroke="#ed1c2a" stroke-width="2.5"/><path d="M13 1 H19 V7Z" fill="#ed1c2a"/></svg>
      <p><b>Aenean</b> ridiculus tortor quis interdum id habitant ad, natoque consectetuer nisl auctor libero quisque euismod ante inceptos malesuada ligula mattis.</p>
    </div>
  </div>
  <footer class="foot"><span class="mark">NIC</span><span class="label">NORTHGATE INVESTMENT COUNCIL</span><span class="page">3</span></footer>
</section>

<section class="slide s4">
  <header class="slide-head">
    <h2>COLOR STYLE TABLES</h2>
    <p>CHOOSE FROM A <b>LIGHT</b> OR <b>DARK</b> THEME</p>
  </header>

  <div class="table-block light">
    <div class="table-title"><svg width="16" height="12" viewBox="0 0 16 12"><rect x="1" y="1" width="14" height="10" fill="none" stroke="#ed1c2a" stroke-width="1.5"/><path d="M1 4.5H15M1 8H15M6 1V11M10.5 1V11" stroke="#ed1c2a" stroke-width="1.2"/></svg><span><b>Light</b> Theme</span></div>
    <table>
      <tr><th>Item</th><th>Step/Action</th><th>Responsible</th><th>Target Date</th></tr>
      <tr><td>1</td><td>Business X, Y, Z high level needs</td><td>Business X, Y, Z</td><td>5/24/2013</td></tr>
      <tr><td>2</td><td>Understand current situation and safety mana</td><td>Business X, Y, Z</td><td>5/31/2013</td></tr>
      <tr><td>3</td><td>Submit Proposal</td><td>Business X, Y, Z</td><td>6/3/2013</td></tr>
      <tr><td>4</td><td>Review Proposal</td><td>Business X, Y, Z</td><td>TBD</td></tr>
      <tr><td>5</td><td>Prepare Final Proposal &amp; Statement of Work (SOW)</td><td>Business X, Y, Z</td><td>TBD</td></tr>
      <tr><td>6</td><td>Complete and sign SOW</td><td>Business X, Y, Z</td><td>TBD</td></tr>
      <tr><td>7</td><td>Schedule project start date</td><td>Business X, Y, Z</td><td>TBD</td></tr>
      <tr><td>8</td><td>Kick-off Project</td><td>Business X, Y, Z</td><td>TBD</td></tr>
      <tr><td>9</td><td>Complete Project</td><td>Business X, Y, Z</td><td>TBD</td></tr>
    </table>
    <div class="tfoot">* Additional Information</div>
  </div>

  <div class="table-block dark">
    <div class="table-title"><svg width="16" height="12" viewBox="0 0 16 12"><rect x="1" y="1" width="14" height="10" fill="none" stroke="#ed1c2a" stroke-width="1.5"/><path d="M1 4.5H15M1 8H15M6 1V11M10.5 1V11" stroke="#ed1c2a" stroke-width="1.2"/></svg><span><b>Dark</b> Theme</span></div>
    <table>
      <tr><th>Item</th><th>Step/Action</th><th>Responsible</th><th>Target Date</th></tr>
      <tr><td>1</td><td>Business X, Y, Z high level needs</td><td>Business X, Y, Z</td><td>5/24/2013</td></tr>
      <tr><td>2</td><td>Understand current situation and safety mana</td><td>Business X, Y, Z</td><td>5/31/2013</td></tr>
      <tr><td>3</td><td>Submit Proposal</td><td>Business X, Y, Z</td><td>6/3/2013</td></tr>
      <tr><td>4</td><td>Review Proposal</td><td>Business X, Y, Z</td><td>TBD</td></tr>
      <tr><td>5</td><td>Prepare Final Proposal &amp; Statement of Work (SOW)</td><td>Business X, Y, Z</td><td>TBD</td></tr>
      <tr><td>6</td><td>Complete and sign SOW</td><td>Business X, Y, Z</td><td>TBD</td></tr>
      <tr><td>7</td><td>Schedule project start date</td><td>Business X, Y, Z</td><td>TBD</td></tr>
      <tr><td>8</td><td>Kick-off Project</td><td>Business X, Y, Z</td><td>TBD</td></tr>
      <tr><td>9</td><td>Complete Project</td><td>Business X, Y, Z</td><td>TBD</td></tr>
    </table>
    <div class="tfoot">* Additional Information</div>
  </div>
  <footer class="foot"><span class="mark">NIC</span><span class="label">NORTHGATE INVESTMENT COUNCIL</span><span class="page">5</span></footer>
</section>

<section class="slide s5">
  <header class="slide-head">
    <h2>COLOR STYLE GRAPHS</h2>
    <p>CHOOSE TO USE BETWEEN <b>MAIN</b> AND <b>SECONDARY</b> COLOR THEMES</p>
  </header>
  <h3 class="graph-title g-main"><b>Graph</b> Main Colors</h3>
  <svg class="chart-area" width="240" height="175" viewBox="0 0 240 175" font-family="Roboto, sans-serif" font-size="7">
    <g fill="#ed1c2a" text-anchor="end">
      <text x="16" y="23">100</text><text x="16" y="59">75</text><text x="16" y="95">50</text><text x="16" y="131">25</text><text x="16" y="167">0</text>
    </g>
    <g stroke="#ed1c2a" stroke-width=".8">
      <line x1="20" y1="20" x2="224" y2="20"/><line x1="20" y1="56" x2="224" y2="56"/><line x1="20" y1="92" x2="224" y2="92"/>
    </g>
    <path d="M38 164 L38 85 L100 102 L162 63 L200 76 L200 164Z" fill="#3a3a3a"/>
    <path d="M38 164 L38 121 L100 128 L130 120 L130 164Z" fill="#9b9b9b"/>
    <path d="M38 164 L38 140 L100 126 L162 87 L224 27 L224 164Z" fill="#ed1c2a"/>
    <line x1="38" y1="164" x2="224" y2="164" stroke="#555" stroke-width=".8"/>
    <g fill="#333" text-anchor="middle"><text x="38" y="173">2007</text><text x="100" y="173">2008</text><text x="162" y="173">2009</text><text x="224" y="173">2010</text></g>
  </svg>

  <h3 class="graph-title g-sec"><b>Graph</b> Secondary Colors</h3>
  <svg class="chart-pie" width="180" height="180" viewBox="0 0 180 180" font-family="Roboto, sans-serif" font-size="9" font-weight="500" fill="#fff">
    <path d="M85 85 L40.8 151.6 A80 80 0 0 1 125 15.7Z" fill="#00a0d6"/>
    <path d="M90.8 79.4 L130.8 10.1 A80 80 0 0 1 161.7 42.3Z" fill="#74bd43" stroke="#fff" stroke-width="1.5"/>
    <path d="M85 85 L155.9 47.9 A80 80 0 0 1 158.8 116Z" fill="#e5723a"/>
    <path d="M85 85 L158.8 116 A80 80 0 0 1 40.8 151.6Z" fill="#9457ae"/>
    <text x="40" y="80">50%</text><text x="129" y="45">9%</text><text x="133" y="92">14%</text><text x="94" y="139">28%</text>
  </svg>
  <div class="legend">
    <span><i style="background:var(--green)"></i>2007</span><span><i style="background:var(--orange)"></i>2008</span>
    <span><i style="background:var(--purple)"></i>2009</span><span><i style="background:var(--blue)"></i>2010</span>
  </div>

  <ul class="bullets b-main">
    <li><b>Aenean</b> ridiculus tortor quis interdum id habitant ad, natoque consectetuer nisl auctor libero quisque euismod ante inceptos malesuada ligula mattis.</li>
    <li>Varius inceptos <b>nascetur</b> mollis dui aptent ultrices. Pretium pulvinar ante lobortis convallis lectus netus vitae penatibus eros at blandit. Parturient.</li>
  </ul>
  <ul class="bullets b-sec">
    <li><b>Aenean</b> ridiculus tortor quis interdum id habitant ad, natoque consectetuer nisl auctor libero quisque euismod ante inceptos malesuada ligula mattis.</li>
    <li>Varius inceptos <b>nascetur</b> mollis dui aptent ultrices. Pretium pulvinar ante lobortis convallis lectus netus vitae penatibus eros at blandit. Parturient.</li>
  </ul>
  <footer class="foot dark"><span class="mark">NIC</span><span class="label">NORTHGATE INVESTMENT COUNCIL</span><span class="page">7</span></footer>
</section>

<section class="slide s6">
  <h1 class="brand-name">Northgate<br>Investment Council</h1>
  <div class="contact">
    <h4>Contact us:</h4>
    <p>555-010-0199</p>
    <p><u>info@northgatecouncil.org</u></p>
    <h4>Central Office:</h4>
    <p>Address Line 1</p>
    <p>Address Line 2</p>
  </div>
  <div class="social">
    <i></i><i></i><i></i>
    <svg width="14" height="10" viewBox="0 0 14 10"><rect width="14" height="10" rx="1" fill="#fff"/><path d="M1 1.5 L7 6 L13 1.5" fill="none" stroke="#ed1c2a" stroke-width="1.3"/></svg>
  </div>
</section>

</body>
</html>
```